Vormetra DHT Blocker label

Updated label size in inches - Rectangle 2.625000 x 7.250000 (2-5/8 x 7-1/4)
UPC has been downloaded.
Label size is label is 2 5/8th x 7 3/8th
Hello - our company develops novel products for the skin, & hair care industry as well as dietary supplements. We're looking for a label design for a new product. The product is a premium hair loss/growth supplement. I attached the brand logo & some competitive product designs that we find attractive.
We need a label design for our Vormetra Hair Loss supplement. It is a natural hair loss supplement for men & women to regrow new hair and help restore hair loss & thinning hair due to vitamin deficiencies, hormone imbalance & aging. It is a science based efficacious supplement with a century’s old medicinal herbal formula.
Attached is our logo & some files of other competition. The label must have an upscale, technology flair to it. The product is clinically effective, leveraged by Ancient Wisdom and Modern Science.
Below are attached files of other generic competition for your perusal.
Updates

I have just uploaded the Vormetra logo files.

Target Market(s)

Men & women suffering from hair loss

Requirements
Must have
• see attached files
Nice to have
• see attached files

```html
<!DOCTYPE html>
<html lang="en">
<head>
<meta charset="utf-8">
<title>Vormetra DHT Blocker label</title>
<link href="https://fonts.googleapis.com/css2?family=Montserrat:ital,wght@0,600;0,700;0,800;0,900;1,500&display=swap" rel="stylesheet">
<style>
  :root {
    --page: #f4f4f6;
    --purple-deep: #3d1260;
    --purple-mid: #5b2282;
    --purple-glow: #8a3fc0;
    --silver-light: #eef0f3;
    --silver-dark: #b4b8c1;
    --gold: #c9963a;
    --gold-light: #f0c766;
    --ink: #1f1f24;
    --white: #ffffff;
  }
  html, body {
    margin: 0;
    padding: 0;
    width: 1200px;
    height: 1200px;
    overflow: hidden;
    background: var(--page);
  }
  .label {
    position: absolute;
    left: 130px;
    top: 45px;
    width: 940px;
    height: 1110px;
    box-shadow: 0 10px 40px rgba(0,0,0,0.12);
  }
  .label svg { display: block; }
  .brand-name {
    font-family: "Montserrat", sans-serif;
    font-weight: 700;
    font-size: 66px;
    fill: var(--ink);
  }
  .tagline {
    font-family: "Montserrat", sans-serif;
    font-weight: 700;
    font-size: 72px;
    fill: var(--silver-light);
  }
  .headline {
    font-family: "Montserrat", sans-serif;
    font-weight: 900;
    fill: url(#silverText);
    stroke: var(--gold);
    stroke-width: 3;
    paint-order: stroke fill;
  }
  .benefit {
    font-family: "Montserrat", sans-serif;
    font-style: italic;
    font-weight: 500;
    font-size: 23px;
    fill: var(--ink);
  }
  .count {
    font-family: "Montserrat", sans-serif;
    font-weight: 800;
    fill: var(--white);
  }
</style>
</head>
<body>
<div class="label">
  <svg width="940" height="1110" viewBox="0 0 940 1110" xmlns="http://www.w3.org/2000/svg">
    <defs>
      <linearGradient id="purpleField" x1="0" y1="0" x2="1" y2="1">
        <stop offset="0" stop-color="var(--purple-deep)"/>
        <stop offset="0.55" stop-color="var(--purple-mid)"/>
        <stop offset="1" stop-color="var(--purple-deep)"/>
      </linearGradient>
      <radialGradient id="purpleGlow" cx="0.45" cy="0.45" r="0.55">
        <stop offset="0" stop-color="var(--purple-glow)" stop-opacity="0.45"/>
        <stop offset="1" stop-color="var(--purple-glow)" stop-opacity="0"/>
      </radialGradient>
      <linearGradient id="silverPanel" x1="0" y1="0" x2="1" y2="0">
        <stop offset="0" stop-color="var(--silver-dark)"/>
        <stop offset="0.35" stop-color="var(--silver-light)"/>
        <stop offset="0.7" stop-color="#d6d9df"/>
        <stop offset="1" stop-color="var(--silver-dark)"/>
      </linearGradient>
      <linearGradient id="silverText" x1="0" y1="0" x2="1" y2="1">
        <stop offset="0" stop-color="#ffffff"/>
        <stop offset="0.5" stop-color="#c9ccd3"/>
        <stop offset="1" stop-color="#eef0f3"/>
      </linearGradient>
      <linearGradient id="goldLine" x1="0" y1="0" x2="1" y2="0">
        <stop offset="0" stop-color="var(--gold)"/>
        <stop offset="0.5" stop-color="var(--gold-light)"/>
        <stop offset="1" stop-color="var(--gold)"/>
      </linearGradient>
    </defs>

    <!-- purple field -->
    <rect class="field" x="0" y="0" width="940" height="1110" fill="url(#purpleField)"/>
    <rect class="field-glow" x="0" y="0" width="940" height="1110" fill="url(#purpleGlow)"/>

    <!-- silver brand panel -->
    <path class="brand-panel" d="M0 0 H680 C610 0 600 70 575 150 C555 215 530 248 480 250 H0 Z" fill="url(#silverPanel)"/>
    <path class="brand-panel-edge" d="M680 0 C610 0 600 70 575 150 C555 215 530 248 480 250 H0" fill="none" stroke="url(#goldLine)" stroke-width="4"/>

    <text class="brand-name" x="168" y="148">Vormetra</text>

    <!-- follicle shield emblem -->
    <path class="emblem" role="img" aria-label="Shield emblem with hair follicle" d="M635 180 Q725 150 815 180 Q815 330 725 392 Q635 330 635 180 Z" fill="#d9dbe0" stroke="var(--gold)" stroke-width="5"/>

    <!-- tagline -->
    <text class="tagline" x="100" y="362">GROWTH</text>
    <text class="tagline" x="100" y="440">ACTIVATOR</text>

    <!-- headline -->
    <text class="headline" x="100" y="735" font-size="340" textLength="604" lengthAdjust="spacingAndGlyphs">DHT</text>
    <text class="headline" x="100" y="868" font-size="146" textLength="597" lengthAdjust="spacingAndGlyphs">BLOCKER</text>

    <!-- silver benefits band -->
    <path class="benefits-panel" d="M0 912 H690 C735 912 745 950 760 1000 C772 1040 790 1050 830 1050 H940 V1110 H0 Z" fill="url(#silverPanel)"/>
    <path class="benefits-panel-edge" d="M0 912 H690 C735 912 745 950 760 1000 C772 1040 790 1050 830 1050 H940" fill="none" stroke="url(#goldLine)" stroke-width="4"/>

    <text class="benefit" x="40" y="968">›› Prevents Hair Loss &amp; Restores Thinning Fragile Hair</text>
    <text class="benefit" x="40" y="998">›› Promotes Natural Hair Growth</text>
    <text class="benefit" x="40" y="1028">›› Visibly Increases Hair Density &amp; Thickness</text>
    <text class="benefit" x="40" y="1058">›› Promotes Follicle Regeneration &amp; Hair Growth</text>

    <!-- count -->
    <text class="count" x="690" y="950"><tspan font-size="38">60</tspan><tspan font-size="26" dx="8">Capsules</tspan></text>
    <text class="count" x="720" y="1004"><tspan font-size="38">30</tspan><tspan font-size="26" dx="8">Supply</tspan></text>
  </svg>
</div>
</body>
</html>
```